Design some Business Cards

Calling all freelancers: Start-up landscaping company needs a logo and business cards.

RTK Landscaping
Sam Riverton, Owner
Mowing- Edging-Trimming
Phone & Text 555-318-7042
If you can grow it, I can MOW it!
Free estimate, call now.

```html
<!DOCTYPE html>
<html lang="en">
<head>
<meta charset="UTF-8">
<title>RTK Landscaping – Business Cards</title>
<link href="https://fonts.googleapis.com/css2?family=Montserrat:wght@400;500;800&display=swap" rel="stylesheet">
<style>
  :root {
    --bg: #e6e8ea;
    --green: #3bb54a;
    --charcoal: #3a3a3a;
    --paper: #f3f3f3;
    --light-text: #d8d8d8;
    --white: #ffffff;
  }
  * { margin: 0; padding: 0; box-sizing: border-box; }
  html, body {
    width: 1200px; height: 900px; overflow: hidden;
    background: var(--bg);
    font-family: "Montserrat", sans-serif;
  }
  .stage {
    width: 1200px; height: 900px;
    display: flex; align-items: center; justify-content: center; gap: 50px;
  }
  .card {
    position: relative;
    width: 540px; height: 309px;
    border-radius: 22px;
    overflow: hidden;
    box-shadow: 0 6px 18px rgba(0,0,0,0.15);
  }
  .card-front {
    background: var(--green);
    display: flex; align-items: center; justify-content: center;
  }
  .brand-name {
    font-weight: 800;
    letter-spacing: 1px;
    text-transform: uppercase;
    text-align: center;
    line-height: 1.15;
    white-space: nowrap;
  }
  .card-front .brand-name { color: var(--white); font-size: 40px; }
  .card-back { background: var(--paper); }
  .card-back svg.panel { position: absolute; inset: 0; }
  .contact-block {
    position: absolute; left: 34px; top: 36px; width: 240px;
  }
  .person-name { color: var(--green); font-size: 24px; font-weight: 400; }
  .person-role { color: var(--light-text); font-size: 17px; font-weight: 400; margin-bottom: 22px; }
  .contact-row {
    display: flex; align-items: center; gap: 10px;
    color: var(--light-text); font-size: 12px; margin-bottom: 10px;
  }
  .contact-icon { width: 20px; height: 20px; flex: none; }
  .card-back .brand-name {
    position: absolute; left: 300px; width: 220px;
    top: 50%; transform: translateY(-50%);
    color: var(--green); font-size: 22px;
  }
</style>
</head>
<body>
<main class="stage">
  <section class="card card-front">
    <p class="brand-name">RTK Landscaping</p>
  </section>

  <section class="card card-back">
    <svg class="panel" width="540" height="309" viewBox="0 0 540 309">
      <path d="M0 0 H240 C305 80 292 230 225 309 H0 Z" fill="var(--charcoal)"/>
      <path d="M240 0 C305 80 292 230 225 309" fill="none" stroke="var(--green)" stroke-width="5"/>
    </svg>

    <div class="contact-block">
      <p class="person-name">Sam Riverton</p>
      <p class="person-role">Owner</p>
      <div class="contact-row">
        <svg class="contact-icon" viewBox="0 0 20 20"><circle cx="10" cy="10" r="10" fill="var(--green)"/><path d="M7 5.5 L8.6 5.5 L9.4 8 L8.3 9 C8.9 10.3 9.8 11.2 11 11.8 L12 10.7 L14.5 11.5 L14.5 13 C14.5 13.8 13.8 14.5 13 14.5 C9.4 14.2 5.8 10.6 5.5 7 C5.5 6.2 6.2 5.5 7 5.5 Z" fill="var(--white)"/></svg>
        <span>555-318-7042 (Phone &amp; Text)</span>
      </div>
      <div class="contact-row">
        <svg class="contact-icon" viewBox="0 0 20 20"><circle cx="10" cy="10" r="10" fill="var(--green)"/><rect x="5" y="6.5" width="10" height="7" fill="var(--white)"/><path d="M5 6.5 L10 10.5 L15 6.5" fill="none" stroke="var(--green)" stroke-width="1"/></svg>
        <span>hello@rtklandscaping.com</span>
      </div>
      <div class="contact-row">
        <svg class="contact-icon" viewBox="0 0 20 20"><circle cx="10" cy="10" r="10" fill="var(--green)"/><g fill="none" stroke="var(--white)" stroke-width="1.1"><circle cx="10" cy="10" r="5"/><ellipse cx="10" cy="10" rx="2.2" ry="5"/><line x1="5" y1="10" x2="15" y2="10"/></g></svg>
        <span>www.rtklandscaping.com</span>
      </div>
    </div>

    <p class="brand-name">RTK<br>Landscaping</p>
  </section>
</main>
</body>
</html>
```